Business Card Design

I would like a double sided business card design.

1 side showing usual contact details and small version of logo (attached "LarkVeil")

other side with larger logo and artwork with room to list what we specialise in.

Lark Veil is a Fashion Millinery Design and Sales Business.

I have attached some other examples of te styles i like so you can see what sort of taste i have.

Feel free to play around with colours of logo - it is grey as i originall had in mind a black background with monochrome silver logo.
Updates

• Please send me a message with your quote after posting your design. Budget set at Minimum (FYI) and negotiable
• Supporting files are examples only - i do not wish to copy them.  The only file for exact use is my logo "LarkVeil"
• Thank you

Target Market(s)

18 - 80 yo females mainly

Industry/Entity Type

Business

Requirements
Must have
• unique and striking individuality
Should not have
• boring and normal

```html
<!DOCTYPE html>
<html lang="en">
<head>
<meta charset="utf-8">
<title>Lark Veil — Business Card</title>
<link rel="stylesheet" href="https://fonts.googleapis.com/css2?family=Raleway:wght@300&family=Open+Sans:wght@300;400&display=swap">
<style>
  :root {
    --paper: #ffffff;
    --card: #000000;
    --ink-light: #f2f2f2;
    --teal: #1fb2a6;
    --cyan: #33c6d8;
    --plume-a: #14a89c;
    --plume-b: #7cc46a;
    --plume-c: #c05c78;
    --crop: #444444;
  }
  html, body {
    margin: 0;
    padding: 0;
    overflow: hidden;
  }
  .sheet {
    position: relative;
    width: 986px;
    height: 1200px;
    background: var(--paper);
    overflow: hidden;
    font-family: "Open Sans", Arial, sans-serif;
  }
  .crop-mark {
    position: absolute;
    background: var(--crop);
  }
  .crop-mark--v { width: 1px; }
  .crop-mark--h { height: 1px; }

  .card {
    position: absolute;
    left: 199px;
    width: 646px;
    height: 373px;
    background: var(--card);
    overflow: hidden;
  }
  .card--front { top: 135px; }
  .card--back { top: 682px; }

  .plumes {
    position: absolute;
    top: 0;
    height: 100%;
    background:
      radial-gradient(ellipse at 40% 25%, rgba(31,178,166,0.85), transparent 55%),
      radial-gradient(ellipse at 70% 55%, rgba(124,196,106,0.6), transparent 60%),
      radial-gradient(ellipse at 30% 80%, rgba(192,92,120,0.45), transparent 60%),
      var(--card);
  }
  .card--front .plumes { left: 400px; width: 246px; }
  .card--back .plumes { left: 0; width: 165px; }

  .brand-vertical {
    position: absolute;
    left: 48px;
    top: 186px;
    transform: translate(-50%, -50%) rotate(-90deg);
    font-family: "Raleway", Arial, sans-serif;
    font-weight: 300;
    font-size: 64px;
    color: var(--ink-light);
    white-space: nowrap;
    line-height: 1;
  }
  .contact {
    position: absolute;
    left: 102px;
    top: 18px;
    color: var(--ink-light);
    font-weight: 300;
    font-size: 23px;
    line-height: 30px;
  }
  .contact p { margin: 0; }
  .contact__name { font-size: 29px; line-height: 36px; }
  .contact__surname { color: var(--teal); }
  .contact__phones { margin-top: 18px !important; }
  .contact__email { margin-top: 30px !important; }
  .contact__web {
    position: absolute;
    left: 102px;
    top: 300px;
    color: var(--cyan);
    font-weight: 300;
    font-size: 26px;
  }

  .brand-large {
    position: absolute;
    left: 158px;
    width: 436px;
    top: 118px;
    text-align: center;
    font-family: "Raleway", Arial, sans-serif;
    font-weight: 300;
    font-size: 92px;
    line-height: 1;
    color: var(--ink-light);
  }
  .brand-rule {
    position: absolute;
    left: 158px;
    top: 230px;
    width: 436px;
    height: 2px;
    background: var(--ink-light);
  }
  .specialty {
    position: absolute;
    left: 158px;
    width: 436px;
    top: 244px;
    text-align: center;
    color: var(--ink-light);
    font-size: 23px;
    font-weight: 400;
  }
</style>
</head>
<body>
<div class="sheet">
  <!-- crop marks, top -->
  <div class="crop-mark crop-mark--v" style="left:204px;top:0;height:97px"></div>
  <div class="crop-mark crop-mark--v" style="left:843px;top:0;height:97px"></div>
  <!-- crop marks, middle -->
  <div class="crop-mark crop-mark--v" style="left:204px;top:552px;height:90px"></div>
  <div class="crop-mark crop-mark--v" style="left:843px;top:552px;height:90px"></div>
  <!-- crop marks, bottom -->
  <div class="crop-mark crop-mark--v" style="left:204px;top:1106px;height:94px"></div>
  <div class="crop-mark crop-mark--v" style="left:843px;top:1106px;height:94px"></div>
  <!-- horizontal marks -->
  <div class="crop-mark crop-mark--h" style="left:77px;top:135px;width:77px"></div>
  <div class="crop-mark crop-mark--h" style="left:77px;top:508px;width:77px"></div>
  <div class="crop-mark crop-mark--h" style="left:77px;top:682px;width:77px"></div>
  <div class="crop-mark crop-mark--h" style="left:77px;top:1054px;width:77px"></div>
  <div class="crop-mark crop-mark--h" style="left:894px;top:135px;width:92px"></div>
  <div class="crop-mark crop-mark--h" style="left:894px;top:508px;width:92px"></div>
  <div class="crop-mark crop-mark--h" style="left:894px;top:682px;width:92px"></div>
  <div class="crop-mark crop-mark--h" style="left:894px;top:1054px;width:92px"></div>

  <section class="card card--front">
    <div class="brand-vertical">LarkVeil</div>
    <div class="contact">
      <p class="contact__name">Mara<span class="contact__surname">Lind</span></p>
      <p>48 Willow Lane</p>
      <p>Harbor, NY, 10000</p>
      <p class="contact__phones">P: 555.201.4477</p>
      <p>F: 555.201.4478</p>
      <p class="contact__email">mara@larkveil.com</p>
    </div>
    <div class="contact__web">www.larkveil.com</div>
    <div class="plumes" role="img" aria-label="Peacock feather plumes illustration in teal, green and rose"></div>
  </section>

  <section class="card card--back">
    <div class="plumes" role="img" aria-label="Peacock feather plumes illustration in teal, green and rose"></div>
    <div class="brand-large">LarkVeil</div>
    <div class="brand-rule"></div>
    <div class="specialty">Fashion Millinery Design &amp; Sales</div>
  </section>
</div>
</body>
</html>
```